Interior Design Company - Project Folder Design

Require simple layout design for company folders in a specific template as attach. Company name is VOLMAR. Tag line is "bring calm into every space" in Microsoft Word <Juice ITC> font type. Corporate colors include dark grey, turqoise and white.
Logo, AI template and some images are attached.

Company focus on Interior Design and Build services. Our services includes all commercial and residential projects.

Target Market(s)

B2B,B2C Corporate and Residential Design, Fit-outs and Project Management

Industry/Entity Type

Interior

Font styles to use
Sans Serif

Colors
33a6d7
333333
ffffff

Requirements
Must have
• Logo
• Address - No. 52 Kerrow Street #04-11, Ferrin Centre, Singapore 179342
• Web - www.volmar-example.com
Nice to have
• Clean professional architectural lines
Should not have
• No cartoons, kiddy images nor repetitive patterns

```html
<!DOCTYPE html>
<html lang="en">
<head>
<meta charset="utf-8">
<title>VOLMAR Project Folder</title>
<link rel="stylesheet" href="https://fonts.googleapis.com/css2?family=Open+Sans:wght@300;400&family=Gochi+Hand&display=swap">
<style>
  :root {
    --backdrop: #d9d9d9;
    --brand-blue: #29a3d8;
    --brand-dark: #050505;
    --brand-turquoise: #3fc1c9;
    --text-light: #e8e8e8;
    --text-muted: #9a9a9a;
    --die-line: #d0343a;
    --photo-dark: #2b2622;
    --photo-mid: #6d5e4e;
    --photo-light: #c9b8a0;
  }
  html, body {
    margin: 0;
    width: 1200px;
    height: 1200px;
    overflow: hidden;
    background: var(--backdrop);
  }
  .folder-dieline {
    position: absolute;
    left: 40px;
    top: 257px;
    width: 1120px;
    height: 685px;
  }
  .brand-name { font-family: "Open Sans", sans-serif; font-weight: 300; fill: var(--text-light); }
  .brand-dot { fill: var(--brand-turquoise); }
  .tagline { font-family: "Gochi Hand", cursive; fill: #cfcfcf; }
  .address { font-family: "Open Sans", sans-serif; font-weight: 400; fill: var(--text-muted); font-size: 7.5px; }
  .die { fill: none; stroke: var(--die-line); stroke-width: 0.8; }
</style>
</head>
<body>
<svg class="folder-dieline" viewBox="135 48 1230 752" xmlns="http://www.w3.org/2000/svg">
  <defs>
    <linearGradient id="roomTones" x1="0" y1="0" x2="1" y2="1">
      <stop offset="0" stop-color="var(--photo-mid)"/>
      <stop offset="0.45" stop-color="var(--photo-dark)"/>
      <stop offset="0.75" stop-color="var(--photo-light)"/>
      <stop offset="1" stop-color="var(--photo-mid)"/>
    </linearGradient>
  </defs>

  <!-- pocket flap -->
  <g class="pocket-flap">
    <rect x="135" y="48" width="231" height="50" fill="var(--brand-blue)"/>
    <rect x="135" y="98" width="248" height="654" fill="var(--brand-blue)"/>
    <polygon points="135,500 296,342 383,425 383,752 135,752" fill="var(--brand-dark)"/>
    <rect x="135" y="752" width="231" height="48" fill="var(--brand-dark)"/>
    <text class="brand-name" x="274" y="446" font-size="22">volmar</text>
    <circle class="brand-dot" cx="351" cy="440" r="3"/>
  </g>

  <!-- cover panel -->
  <g class="cover-panel">
    <rect x="383" y="98" width="982" height="654" fill="url(#roomTones)" role="img" aria-label="Photograph of a modern bedroom interior at night with upholstered headboard, wooden bed base and city view window"/>
    <polygon points="383,440 680,752 383,752" fill="var(--brand-dark)"/>
    <polygon points="1228,497 1365,630 1365,752 968,752" fill="var(--brand-dark)"/>

    <text class="brand-name" x="415" y="677" font-size="15">volmar</text>
    <circle class="brand-dot" cx="466" cy="672" r="2"/>
    <text class="address" x="415" y="699">No. 52 Kerrow Street #04-11,</text>
    <text class="address" x="415" y="709">Ferrin Centre, Singapore 179342</text>
    <text class="address" x="415" y="719">www.volmar-example.com</text>

    <text class="brand-name" x="1196" y="649" font-size="32">volmar</text>
    <circle class="brand-dot" cx="1302" cy="641" r="4"/>
    <text class="tagline" x="1060" y="703" font-size="23">bring calm into every space</text>
  </g>

  <!-- die lines -->
  <g class="die">
    <rect x="135" y="48" width="231" height="752"/>
    <line x1="135" y1="98" x2="366" y2="98"/>
    <line x1="135" y1="752" x2="366" y2="752"/>
    <rect x="383" y="98" width="982" height="654"/>
    <line x1="366" y1="98" x2="366" y2="752"/>
    <line x1="865" y1="98" x2="865" y2="752"/>
    <line x1="882" y1="98" x2="882" y2="752"/>
    <path d="M168,625 Q155,655 168,685"/>
    <path d="M265,625 Q245,655 265,685"/>
    <path d="M345,625 Q330,655 345,685"/>
    <path d="M210,712 Q250,690 292,712"/>
  </g>
</svg>
</body>
</html>
```